Business Card Design Project

New Private residential substance abuse treatment facility in Mapleton, UT. Facility located in elegant 11,000 home with stunning views of the mountains. Wish to incorporate colored logo. Business name- Birchwell Harbor Wellness. Facility is Tudor style with traditional furnishings, an overhead picture is attached. Lettering in a simple scroll or old english style. Must be easy to read with clear moderetly large font.
Updates

It seems the project time frame listed was not correct- it is a week.

Target Market(s)

Adults 18 and over with substance abuse issues requiring residential rehabilitation. Referral base are medical/mental health professionals, families and community agencies.

Industry/Entity Type

Residential

Colors
9bcb3b
fece3e
fbee3f

Requirements
Must have
• Clear and easy to read, professional and upscale presentation. Need logo, name, title, address, phone, fax and web page address. May add slogan later. Use same font as logo.
Nice to have
• Logo has a green mountain and a gold maple leaf so a nature themed element may work. Want to promote peaceful grounded image. Logo attached.
Should not have
• No tiny or complicated font. No modern or tech looking images. No light colored fonts.

```html
<!DOCTYPE html>
<html lang="en">
<head>
<meta charset="utf-8">
<title>Birchwell Harbor Wellness – Business Card</title>
<link rel="stylesheet" href="https://fonts.googleapis.com/css2?family=Play:wght@400;700&family=Tinos:ital,wght@1,700&display=swap">
<style>
  :root {
    --forest: #3f6428;
    --gold: #b08036;
    --ink: #333333;
    --paper: #ffffff;
    --backdrop: #ffffff;
    --card-shadow: rgba(0, 0, 0, 0.6);
    --foliage-light: #e3eadb;
    --foliage-mid: #9db185;
  }
  * { box-sizing: border-box; margin: 0; padding: 0; }
  html, body {
    width: 1200px; height: 900px; overflow: hidden;
    background: var(--backdrop);
  }
  .card {
    position: absolute; left: 82px; top: 110px;
    width: 1062px; height: 645px;
    background: var(--paper);
    box-shadow: 12px 12px 9px var(--card-shadow);
    font-family: "Play", sans-serif;
    color: var(--ink);
    overflow: hidden;
  }
  .brand-name {
    position: absolute; left: 50px; top: 58px;
    font-size: 46px; line-height: 52px; font-weight: 400; color: var(--ink);
    white-space: nowrap;
  }
  .slogan {
    position: absolute; left: 50px; top: 186px;
    font-family: "Tinos", serif; font-style: italic; font-weight: 700;
    font-size: 20px; color: var(--ink); white-space: nowrap;
  }
  .rule { position: absolute; height: 3px; background: var(--forest); top: 247px; }
  .rule--long { left: 48px; width: 524px; }
  .rule--short { left: 948px; width: 74px; }
  .job-title {
    position: absolute; left: 590px; top: 226px;
    font-size: 34px; line-height: 40px; font-weight: 400; color: var(--ink); white-space: nowrap;
  }
  .person { position: absolute; left: 78px; top: 294px; }
  .person-name { font-size: 40px; line-height: 46px; font-weight: 700; margin-bottom: 12px; }
  .contact-line { font-size: 18px; line-height: 20px; font-weight: 700; margin-bottom: 18px; white-space: nowrap; }
  .contact-line--email { font-size: 17px; font-weight: 400; }
  .social {
    position: absolute; left: 565px; top: 300px; width: 480px; height: 140px;
    color: var(--forest); font-size: 19px; font-weight: 700;
  }
  .social-invite { position: absolute; left: 0; top: 19px; white-space: nowrap; }
  .social-square {
    position: absolute; left: 213px; top: 0; width: 58px; height: 58px;
    border: 2px solid var(--forest); border-radius: 8px;
  }
  .social-circle {
    position: absolute; left: 216px; top: 78px; width: 52px; height: 52px;
    border-radius: 50%; background: var(--forest);
  }
  .social-handle { position: absolute; left: 285px; white-space: nowrap; }
  .social-handle--page { top: 19px; }
  .social-handle--feed { top: 86px; }
  .office {
    position: absolute; right: 40px; top: 462px;
    text-align: right; color: var(--ink); font-size: 17px; line-height: 28px;
  }
  .office-line { white-space: nowrap; }
  .meadow {
    position: absolute; left: 0; top: 420px; width: 640px; height: 185px;
    background: radial-gradient(ellipse 75% 100% at 45% 100%, var(--foliage-mid) 0%, var(--foliage-light) 55%, rgba(255,255,255,0) 100%);
  }
  .footer-bands { position: absolute; left: 0; top: 603px; }
  .website {
    position: absolute; left: 48px; top: 607px;
    color: var(--paper); font-size: 25px; line-height: 34px; font-weight: 700; white-space: nowrap;
  }
</style>
</head>
<body>
  <main class="card">
    <div class="brand-name">Birchwell Harbor<br>Wellness</div>
    <p class="slogan">Saving the Birchwell Harbor slogan will be here</p>

    <div class="rule rule--long"></div>
    <h2 class="job-title">Chief executive officer</h2>
    <div class="rule rule--short"></div>

    <section class="person">
      <h1 class="person-name">Professor L</h1>
      <p class="contact-line">OFC 312 - 555 - 0148</p>
      <p class="contact-line">+61400 555 218</p>
      <p class="contact-line contact-line--email">birchwellharbor@mailbox.com</p>
    </section>

    <section class="social">
      <span class="social-invite">Join our campaing on</span>
      <span class="social-square"></span>
      <span class="social-handle social-handle--page">/birchwellharbor</span>
      <span class="social-circle"></span>
      <span class="social-handle social-handle--feed">@birchwellharbor</span>
    </section>

    <address class="office">
      <p class="office-line">FAX 312 - 555 - 0149</p>
      <p class="office-line">1480 Canyon Ridge Road, Mapleton, UT</p>
    </address>

    <div class="meadow" role="img" aria-label="Green silhouette of grasses, wildflowers and trees along the bottom edge"></div>

    <svg class="footer-bands" width="1062" height="42" viewBox="0 0 1062 42" aria-hidden="true">
      <polygon points="0,0 632,0 590,42 0,42" fill="var(--forest)"/>
      <polygon points="658,0 1062,0 1062,42 616,42" fill="var(--gold)"/>
    </svg>
    <p class="website">Visit our website: www.birchwellharbor.com</p>
  </main>
</body>
</html>
```